Ginger Beer Can Design for a none alcoholic bavarage

We need a cool, modern, fresh design for a can.

- 330ml sleek can size
- 0.0% alcohol
- BIO
- ingredience: Water, Sugar, Ginger, limejuice, Gummi Arabicum, Carbonisation
- Energy table of fats, carbs, protein, etc.
- address: Quiet Meadow Drinks, Lindenweg 42, 4052 Basel

```html
<!DOCTYPE html>
<html lang="en">
<head>
<meta charset="utf-8">
<title>Ginger Beer – Can Label</title>
<link href="https://fonts.googleapis.com/css2?family=Staatliches&family=Barlow+Condensed:wght@500;600;700&family=Archivo+Narrow:wght@400;700&display=swap" rel="stylesheet">
<style>
  :root{
    --bg:#ececec;
    --label-cream:#e4e1d8;
    --label-cream-dark:#d3d0c6;
    --brand-green:#2e6a3f;
    --bio-green:#98c257;
    --ink-cream:#eeebe3;
  }
  *{box-sizing:border-box;margin:0;padding:0}
  html,body{width:1200px;height:800px;overflow:hidden;background:var(--bg)}
  .can-wrap{
    position:absolute;left:50px;top:120px;width:1100px;height:560px;
    border-radius:10px;overflow:hidden;
    background:linear-gradient(90deg,var(--label-cream-dark) 0%,var(--label-cream) 18%,#efece5 32%,var(--label-cream) 48%,var(--label-cream-dark) 62%,var(--label-cream) 78%,#efece5 90%,var(--label-cream-dark) 100%);
    color:var(--brand-green);
    font-family:"Barlow Condensed",sans-serif;
  }
  .green-band{position:absolute;left:0;top:0;width:480px;height:560px}

  /* front panel */
  .front{position:absolute;left:0;top:0;width:480px;height:560px}
  .front__tag{
    position:absolute;top:40px;left:0;width:480px;text-align:center;
    font-weight:600;font-size:22px;letter-spacing:2px;
  }
  .front__tag::before,.front__tag::after{
    content:"";display:inline-block;width:40px;height:2px;background:var(--brand-green);
    vertical-align:middle;margin:0 12px;
  }
  .front__title{
    position:absolute;top:72px;left:0;width:480px;text-align:center;
    font-family:"Staatliches",sans-serif;font-weight:400;font-size:130px;line-height:112px;letter-spacing:2px;
  }
  .front__brand{
    position:absolute;top:378px;left:150px;width:180px;text-align:center;
    font-weight:700;font-size:26px;line-height:28px;letter-spacing:2px;color:var(--ink-cream);
  }
  .front__volume{
    position:absolute;left:36px;top:495px;font-weight:600;font-size:20px;color:var(--ink-cream);
  }
  .bio-mark{display:block;background:var(--bio-green)}
  .front__bio{position:absolute;left:385px;top:420px;text-align:center;color:var(--ink-cream);font-weight:600;font-size:16px}
  .front__bio .bio-mark{width:62px;height:42px;margin-bottom:6px}

  /* back panel */
  .nutrition{
    position:absolute;left:520px;top:40px;width:250px;
    border:2px solid var(--brand-green);padding:6px 8px;
    font-family:"Archivo Narrow",sans-serif;font-size:13px;
  }
  .nutrition__title{font-weight:700;font-size:28px;line-height:30px}
  .nutrition__serving{font-weight:700;font-size:17px;border-bottom:9px solid var(--brand-green);padding-bottom:3px}
  .nutrition__amount{font-size:11px;padding-top:3px}
  .nutrition__calories{display:flex;justify-content:space-between;font-weight:700;font-size:26px;line-height:28px;border-bottom:5px solid var(--brand-green)}
  .nutrition__dv{text-align:right;font-weight:700;font-size:11px;border-bottom:1px solid var(--brand-green);padding:2px 0}
  .nutrition__row{display:flex;justify-content:space-between;border-bottom:1px solid var(--brand-green);padding:3px 0}
  .nutrition__row--indent{padding-left:14px}
  .nutrition__row--last{border-bottom:8px solid var(--brand-green)}
  .nutrition__note{font-size:9px;line-height:11px;padding-top:4px}
  .nutrition__foot{font-size:10px;border-top:1px solid var(--brand-green);margin-top:4px;padding-top:3px}
  .ingredients{position:absolute;left:520px;top:420px;width:250px;color:var(--brand-green);font-size:16px;line-height:19px;font-weight:500}
  .ingredients strong{font-weight:700;letter-spacing:1px}

  /* side panel */
  .side{position:absolute;left:800px;top:0;width:300px;height:560px}
  .side__name{position:absolute;left:30px;top:52px;font-weight:700;font-size:34px;letter-spacing:1px;line-height:34px}
  .side__sub{position:absolute;left:30px;top:88px;font-weight:500;font-size:17px;letter-spacing:2px;border-top:2px solid var(--bio-green);padding-top:4px;width:190px}
  .side__bio{position:absolute;left:30px;top:130px;width:62px;height:42px}
  .side__abv{
    position:absolute;left:110px;top:128px;border:2px solid var(--brand-green);
    padding:2px 8px;text-align:center;font-weight:700;font-size:22px;line-height:22px;
  }
  .side__abv small{display:block;font-size:11px;letter-spacing:1px;line-height:12px}
  .side__address{
    position:absolute;left:210px;top:30px;width:300px;
    transform-origin:0 0;transform:translate(0,330px) rotate(-90deg);
    font-weight:500;font-size:16px;line-height:20px;
  }
  .side__brand-vertical{
    position:absolute;left:262px;top:30px;width:300px;
    transform-origin:0 0;transform:translate(0,330px) rotate(-90deg);
    font-weight:700;font-size:18px;letter-spacing:2px;
  }
</style>
</head>
<body>
<main class="can-wrap">
  <svg class="green-band" viewBox="0 0 480 560" aria-hidden="true">
    <path d="M0 405 L146 375 C156 342 196 322 240 322 C284 322 324 342 334 375 L480 375 L480 560 L0 560 Z" fill="var(--brand-green)"/>
    <circle cx="240" cy="420" r="86" fill="none" stroke="var(--ink-cream)" stroke-width="3"/>
  </svg>

  <section class="front">
    <p class="front__tag">NON ALCOHOLIC</p>
    <h1 class="front__title">GINGER<br>BEER</h1>
    <p class="front__brand">QUIET<br>MEADOW<br>DRINKS</p>
    <div class="front__bio"><span class="bio-mark" role="img" aria-label="Organic certification badge"></span>BIO</div>
    <p class="front__volume">330 ML</p>
  </section>

  <section class="nutrition">
    <p class="nutrition__title">Nutrition Facts</p>
    <p class="nutrition__serving">Serving size: 1 Can</p>
    <p class="nutrition__amount">Amount per serving</p>
    <p class="nutrition__calories"><span>Calories</span><span>60</span></p>
    <p class="nutrition__dv">%DV*</p>
    <p class="nutrition__row"><span>Total Fat 0g</span><span>0%</span></p>
    <p class="nutrition__row"><span>Sodium 10mg</span><span>0%</span></p>
    <p class="nutrition__row"><span>Total Carbohydrate 15g</span><span>5%</span></p>
    <p class="nutrition__row nutrition__row--indent"><span>Total Sugars 14g</span><span></span></p>
    <p class="nutrition__row nutrition__row--indent"><span>Incl. 14g Added Sugars</span><span>27%</span></p>
    <p class="nutrition__row nutrition__row--last"><span>Protein 0g</span><span></span></p>
    <p class="nutrition__note">Not a significant source of saturated fat, trans fat, cholesterol, dietary fiber, vitamin D, calcium, iron and potassium.</p>
    <p class="nutrition__foot">%DV = %Daily Value</p>
  </section>

  <p class="ingredients"><strong>INGREDIENTS:</strong><br>Water, Sugar, Ginger, limejuice, Gummi Arabicum, Carbonisation</p>

  <section class="side">
    <p class="side__name">GINGER BEER</p>
    <p class="side__sub">NON ALCOHOLIC</p>
    <span class="bio-mark side__bio" role="img" aria-label="Organic certification badge"></span>
    <p class="side__abv">0.0%<small>ALCOHOL</small></p>
    <p class="side__address">Lindenweg 42, 4052 Basel<br>www.quietmeadowdrinks.ch</p>
    <p class="side__brand-vertical">QUIET MEADOW DRINKS</p>
  </section>
</main>
</body>
</html>
```